Bright Harbor Fitness - Boxing/Adventure training flyer

We are launching our Boxing Fitness business in Brisbane, Australia. We have 15 years experience been fighters and also in training people in fitness using boxing techniques and core strength exercises. We have become tired of seeing trainers 'teaching' boxing to clients and it not been accurate or providing the best exercise in each punch for the client. We also want to make classes about us helping clients to achieve personal fitness goals and also having some fun and socialsing at the same time.
We will be providing adventure goals which may include hiking up a local mountain, mini triathlons or obstacle courses to enable clients to see and feel the fitness they have achieved.
We are really looking for something very professional in look but shows that we are not just another personal training franchise trying to just take a clients money. We want to convey if you come work with us it will be an experience, you will get to know us and feel that you are not just paying your money and working up a sweat you are achieving goals and it is exciting to come to training because you will learn something new each time.

The colours of the business are red, blue and white. I have a pdf of our business card to show you the colours and font we would prefer. I can forward this if necessary.
Updates

Hello,

Thank you for all those who have posted designs for our flyer.

I have uploaded a file with some photos that we would like to be used in the flyer as we seem to have issues in getting what we want so we thought we would find some we like.

We are really hoping to get some great designs with only one day left in our competition, we have some designers changing some things around but if we don't get what we are looking for we will be looking to extend the deadline by a day or two as we really hope there are some designers out there with some great ideas.

Target Market(s)

Looking to target young to middle aged females and males who want to become fit or already have a fitness level but are looking for a challenge

Industry/Entity Type

Training

Requirements
Must have
• Info to have on flyer -
- Classes - $12 for one off class
- $10 when booking 2 or more in a week
Able to book and pay for classes on line, class shedules available online
Only 14 clients to a class
Classes held at Larkspur Rise and Wexford State School - private and secure locations.
About us -
Boxing fitness incorporating pad work, core strength, agility, circuit training, bush track and stair work.
BHF training is a place to set and achieve personal goals in a fun, social and challenging environment.
With 15 years fighting and training experienece we are driven by a passion to help clients achieve fitness goals.

Also provide amatuer and professional training and sparring in a seperate class, personal training.

Need to have some reference for people to visit our website for more detailed info on classes, booking online, etc.

Business name is Bright Harbor Fitness.

Moto is 'Life's a fight be prepared'

also can be used - 'Fitness with attitude'

Start date for classes is 9th July, 2012

Web address is www.brightharborfitness.com.au
Contact number: 0482 316 702
Email: info@brightharborfitness.com.au
Nice to have
• Interesting way of formating wording and pictures to really stand out and get our point accross easily and really make them want to visit the website to find out more.
Should not have
• We are a boxing fitness business but we are looking to offer personal training, group fitness, corporate fitness, elite sports training and helping people to obtain fitness for army, police or firefighter exams therefore we do want some elimate of boxing in the flyer but not overwhelmingly boxing related. More a feel of fitness in general with a boxing aspect.

```html
<!DOCTYPE html>
<html lang="en">
<head>
<meta charset="utf-8">
<title>Bright Harbor Fitness – Boxing &amp; Adventure Training Flyer</title>
<link href="https://fonts.googleapis.com/css2?family=Archivo+Black&family=Arimo:wght@700&family=Open+Sans:ital,wght@0,600;0,700;1,400&family=Gochi+Hand&display=swap" rel="stylesheet">
<style>
  :root {
    --red: #e21f26;
    --navy: #17204f;
    --blue: #1a5fa8;
    --sky: #2fa3d8;
    --ink: #1c1c1c;
    --white: #ffffff;
    --page: #e9e7e4;
    --shadow: rgba(0,0,0,0.28);
  }
  * { box-sizing: border-box; margin: 0; padding: 0; }
  html, body { width: 1200px; height: 900px; overflow: hidden; background: var(--page); }
  body { position: relative; font-family: "Open Sans", Arial, sans-serif; color: var(--ink); }

  .flyer {
    position: absolute; left: 138px; top: 123px; width: 924px; height: 652px;
    background: var(--white); overflow: hidden;
    box-shadow: 0 10px 30px var(--shadow);
  }

  /* Brand block */
  .brand {
    position: absolute; left: 28px; top: 58px; width: 140px;
    display: flex; flex-direction: column; align-items: center; gap: 8px;
  }
  .brand-mark { width: 44px; height: 44px; background: var(--navy); }
  .brand-name {
    font-family: "Arimo", Arial, sans-serif; font-weight: 700; font-size: 16px;
    line-height: 1.1; color: var(--navy); text-align: center;
  }

  /* Header */
  .title {
    position: absolute; left: 180px; top: 14px; width: 730px; text-align: center;
    white-space: nowrap;
    font-family: "Archivo Black", Arial, sans-serif; font-size: 43px; letter-spacing: 0;
    color: var(--red); -webkit-text-stroke: 2.5px var(--ink); paint-order: stroke fill;
    line-height: 1.1;
  }
  .web {
    position: absolute; left: 190px; top: 66px; width: 710px; text-align: center;
    white-space: nowrap;
    font-family: "Arimo", Arial, sans-serif; font-weight: 700; font-size: 31px;
    color: var(--blue); line-height: 1.1;
  }
  .about {
    position: absolute; left: 200px; top: 106px; width: 700px;
    font-style: italic; font-size: 12.5px; line-height: 1.38; color: var(--ink);
    white-space: nowrap;
  }
  .about p:first-child { padding-left: 24px; }

  /* Info cards */
  .card {
    position: absolute; z-index: 3; background: var(--white); border: 1px solid #d5d5d5;
    border-radius: 26px; box-shadow: 4px 6px 10px var(--shadow);
  }
  .features { left: 46px; top: 187px; width: 364px; height: 230px; padding: 12px 4px 0 12px; }
  .features ul { list-style: none; }
  .features li {
    display: flex; gap: 6px; font-weight: 700; font-size: 13px; line-height: 19px;
    letter-spacing: -0.1px; margin-bottom: 5px; white-space: nowrap;
  }
  .features li span.wrap { text-align: center; }
  .tick { flex: none; width: 14px; height: 14px; margin-top: 3px; }

  .schedule {
    left: 456px; top: 202px; width: 378px; height: 198px;
    text-align: center; padding-top: 30px; font-weight: 700; font-size: 16px; line-height: 1.5;
  }
  .start-date {
    font-family: "Gochi Hand", cursive; font-weight: 400; font-size: 28px;
    color: var(--red); line-height: 1.3; margin: 2px 0 4px;
  }
  .venue { color: var(--red); }

  /* Price burst */
  .price-burst { position: absolute; z-index: 4; left: 752px; top: 160px; width: 172px; height: 172px; }
  .price-text {
    position: absolute; z-index: 5; left: 768px; top: 188px; width: 140px; text-align: center;
    color: var(--white); font-family: "Arimo", Arial, sans-serif; font-weight: 700;
    transform: rotate(14deg); line-height: 1.05;
  }
  .price-text .amount { font-size: 40px; }
  .price-text .per { font-size: 18px; }
  .price-text .note { font-size: 11px; margin-top: 2px; }

  /* Photo strip */
  .photos { position: absolute; z-index: 1; left: 0; top: 455px; width: 924px; height: 190px; display: flex; }
  .photo { height: 100%; }
  .photo-class   { width: 215px; background: linear-gradient(135deg, #b5524e, #6b2b2a); }
  .photo-gloves  { width: 115px; background: linear-gradient(160deg, #9a9a9a, #3a3a3a); }
  .photo-boxer   { width: 227px; background: linear-gradient(150deg, #55607e, #1f2436); }
  .photo-core    { width: 122px; background: linear-gradient(170deg, #7d7d7d, #1e1e1e); }
  .photo-punch   { width: 245px; background: linear-gradient(120deg, #e8a3a0, #c9494a); }

  .waves { position: absolute; z-index: 2; left: 0; top: 388px; width: 924px; height: 120px; }
  .base-line { position: absolute; z-index: 6; left: 0; bottom: 0; width: 924px; height: 7px; background: var(--red); }

  .contact {
    position: absolute; z-index: 6; left: 8px; top: 572px; color: var(--white);
    font-weight: 700; font-size: 12.5px; line-height: 1.45; text-shadow: 0 1px 2px #000;
    white-space: nowrap;
  }
  .motto {
    position: absolute; z-index: 6; left: 330px; top: 572px; width: 585px; text-align: right;
    white-space: nowrap;
    font-family: "Gochi Hand", cursive; font-size: 48px; color: var(--white);
    -webkit-text-stroke: 4px var(--ink); paint-order: stroke fill; line-height: 1.2;
  }
</style>
</head>
<body>
<main class="flyer">
  <div class="brand">
    <div class="brand-mark"></div>
    <div class="brand-name">Bright Harbor Fitness</div>
  </div>

  <h1 class="title">BRIGHT HARBOR FITNESS</h1>
  <div class="web">www.brightharborfitness.com.au</div>
  <div class="about">
    <p>Boxing fitness incorporating pad work, core strength, agility, circuit training, bush track and stair work.</p>
    <p>BHF training is a place to set and achieve personal goals in a fun, social and challenging environment.</p>
    <p>With 15 years fighting and training experience we are driven by a passion to help clients achieve fitness goals.</p>
  </div>

  <div class="photos">
    <div class="photo photo-class" role="img" aria-label="Group boxing class training on bags in a brick-walled gym"></div>
    <div class="photo photo-gloves" role="img" aria-label="Boxer in gloves holding a guard stance"></div>
    <div class="photo photo-boxer" role="img" aria-label="Woman boxer throwing a jab toward the camera"></div>
    <div class="photo photo-core" role="img" aria-label="Athlete's toned midsection showing core strength"></div>
    <div class="photo photo-punch" role="img" aria-label="Close-up of a boxing glove landing a punch on a pad"></div>
  </div>

  <svg class="waves" viewBox="0 0 924 120" preserveAspectRatio="none" aria-hidden="true">
    <path fill="#17204f" d="M0,4 C120,40 260,64 420,58 C600,52 760,20 924,12 L924,70 C760,70 600,92 420,96 C250,100 110,80 0,60 Z"/>
    <path fill="#2fa3d8" d="M0,56 C140,82 280,96 440,92 C620,88 780,66 924,72 L924,84 C780,80 620,100 440,104 C280,108 140,94 0,70 Z"/>
    <path fill="none" stroke="#7cc8ea" stroke-width="3" d="M0,48 C160,78 330,84 500,68 C660,54 800,48 924,56"/>
    <path fill="none" stroke="#1a5fa8" stroke-width="5" d="M0,84 C180,104 340,72 520,70 C700,68 820,86 924,90"/>
  </svg>

  <section class="card features">
    <ul>
      <li><svg class="tick" viewBox="0 0 16 16"><circle cx="8" cy="8" r="8" fill="#e21f26"/><path d="M4 8.3l2.6 2.6L12 5.3" stroke="#fff" stroke-width="2.2" fill="none"/></svg><span>$12 for one off class</span></li>
      <li><svg class="tick" viewBox="0 0 16 16"><circle cx="8" cy="8" r="8" fill="#e21f26"/><path d="M4 8.3l2.6 2.6L12 5.3" stroke="#fff" stroke-width="2.2" fill="none"/></svg><span>Only 14 clients to a class</span></li>
      <li><svg class="tick" viewBox="0 0 16 16"><circle cx="8" cy="8" r="8" fill="#e21f26"/><path d="M4 8.3l2.6 2.6L12 5.3" stroke="#fff" stroke-width="2.2" fill="none"/></svg><span>Class shedules available online</span></li>
      <li><svg class="tick" viewBox="0 0 16 16"><circle cx="8" cy="8" r="8" fill="#e21f26"/><path d="M4 8.3l2.6 2.6L12 5.3" stroke="#fff" stroke-width="2.2" fill="none"/></svg><span>Able to book and pay for classes on line</span></li>
      <li><svg class="tick" viewBox="0 0 16 16"><circle cx="8" cy="8" r="8" fill="#e21f26"/><path d="M4 8.3l2.6 2.6L12 5.3" stroke="#fff" stroke-width="2.2" fill="none"/></svg><span class="wrap">We provide amatuer and professional training<br>and sparring in a separate class</span></li>
      <li><svg class="tick" viewBox="0 0 16 16"><circle cx="8" cy="8" r="8" fill="#e21f26"/><path d="M4 8.3l2.6 2.6L12 5.3" stroke="#fff" stroke-width="2.2" fill="none"/></svg><span class="wrap">Adventure goals like hiking up a local mountain,<br>mini triathlons or obstacle courses</span></li>
      <li><svg class="tick" viewBox="0 0 16 16"><circle cx="8" cy="8" r="8" fill="#e21f26"/><path d="M4 8.3l2.6 2.6L12 5.3" stroke="#fff" stroke-width="2.2" fill="none"/></svg><span>Personal training</span></li>
    </ul>
  </section>

  <section class="card schedule">
    <div>Start date for classes is</div>
    <div class="start-date">9th July, 2012</div>
    <div>Classes held at</div>
    <div><span class="venue">Larkspur Rise</span> and <span class="venue">Wexford State School</span></div>
    <div>private and secure locations</div>
  </section>

  <svg class="price-burst" viewBox="-86 -86 172 172" aria-hidden="true">
    <polygon fill="#dcdcdc" points="0,-84 11,-66 31,-78 35,-57 58,-61 53,-40 75,-36 62,-19 81,-7 64,6 79,22 59,28 68,49 46,48 47,70 27,63 18,83 4,66 -14,82 -22,62 -42,72 -43,50 -65,53 -57,33 -77,26 -61,11 -79,-4 -62,-17 -75,-35 -53,-40 -58,-61 -37,-57 -33,-78 -12,-66"/>
    <polygon fill="#1a5fa8" transform="scale(0.86)" points="0,-84 11,-66 31,-78 35,-57 58,-61 53,-40 75,-36 62,-19 81,-7 64,6 79,22 59,28 68,49 46,48 47,70 27,63 18,83 4,66 -14,82 -22,62 -42,72 -43,50 -65,53 -57,33 -77,26 -61,11 -79,-4 -62,-17 -75,-35 -53,-40 -58,-61 -37,-57 -33,-78 -12,-66"/>
  </svg>
  <div class="price-text">
    <div class="amount">$10</div>
    <div class="per">for 1 class</div>
    <div class="note">(when booking 2<br>or more in a week)</div>
  </div>

  <div class="contact">
    For more details:<br>
    www.brightharborfitness.com.au<br>
    Contact: 0482 316 702<br>
    info@brightharborfitness.com.au
  </div>
  <div class="motto">Life's a fight, be prepared!</div>

  <div class="base-line"></div>
</main>
</body>
</html>
```